We require a banner design for a 53' x 10' trailer for a future development to be displayed on the side of the highway. The development name is 712 35 Commerce Park, logo is attached. This is an industrial future development. Please also include the RLW Group logo and MERO Development logos as well.

Industry/Entity Type

Real Estate / Construction / Developer / Industrial Future Development

Requirements
Must have
• Logos provided

```html
<!DOCTYPE html>
<html lang="en">
<head>
<meta charset="utf-8">
<title>712 35 Commerce Park – Trailer Banner</title>
<link href="https://fonts.googleapis.com/css2?family=Montserrat:wght@500;700&family=Saira+Condensed:wght@800&display=swap" rel="stylesheet">
<style>
  :root {
    --page-bg: #bdbdbd;
    --panel-white: #ffffff;
    --brand-brown: #5a4a40;
    --brand-brown-dark: #4e3f36;
    --ink-dark: #231f20;
    --ink-light: #ffffff;
    --photo-steel: #6f8397;
    --photo-sky: #e9e4d6;
    --photo-warm: #f3e7c8;
  }
  * { margin: 0; padding: 0; box-sizing: border-box; }
  html, body {
    width: 1200px;
    height: 800px;
    overflow: hidden;
    background: var(--page-bg);
  }
  .banner {
    position: absolute;
    left: 40px;
    top: 294px;
    width: 1120px;
    height: 212px;
    background: var(--panel-white);
    overflow: hidden;
  }
  .banner-shapes {
    position: absolute;
    inset: 0;
    width: 1120px;
    height: 212px;
  }
  .brand-block {
    position: absolute;
    left: 30px;
    top: 26px;
    width: 220px;
    text-align: center;
    font-family: "Montserrat", sans-serif;
    font-weight: 700;
    color: var(--ink-dark);
  }
  .brand-number {
    font-size: 50px;
    line-height: 46px;
    letter-spacing: 1px;
  }
  .brand-descriptor {
    margin-top: 6px;
    font-size: 16px;
    letter-spacing: 2.5px;
  }
  .partner-row {
    margin-top: 12px;
    display: flex;
    justify-content: center;
    align-items: center;
    gap: 16px;
    font-size: 13px;
    letter-spacing: 1px;
  }
  .partner {
    display: flex;
    align-items: center;
    gap: 5px;
  }
  .partner-dot {
    width: 9px;
    height: 9px;
    border-radius: 50%;
    background: var(--ink-dark);
  }
  .partner-square {
    width: 9px;
    height: 9px;
    background: var(--ink-dark);
  }
  .headline {
    position: absolute;
    left: 300px;
    top: 22px;
    width: 390px;
    text-align: center;
    font-family: "Saira Condensed", sans-serif;
    font-weight: 800;
    font-size: 56px;
    line-height: 54px;
    color: var(--ink-light);
    text-transform: uppercase;
    letter-spacing: 0.5px;
  }
</style>
</head>
<body>
  <div class="banner">
    <svg class="banner-shapes" viewBox="0 0 1120 212" aria-hidden="false">
      <defs>
        <linearGradient id="photo-tone" x1="0" y1="0" x2="1" y2="0">
          <stop offset="0" stop-color="var(--photo-steel)"/>
          <stop offset="0.55" stop-color="#9aa6ad"/>
          <stop offset="1" stop-color="var(--photo-warm)"/>
        </linearGradient>
        <linearGradient id="brown-tone" x1="0" y1="0" x2="1" y2="0">
          <stop offset="0" stop-color="var(--brand-brown)"/>
          <stop offset="1" stop-color="var(--brand-brown-dark)"/>
        </linearGradient>
      </defs>
      <polygon class="headline-field" points="301,0 752,0 696,106 752,212 301,212 252,106" fill="url(#brown-tone)"/>
      <polygon class="photo-field" role="img" aria-label="Photo of a modern industrial facility with steel storage tanks, pipework and people walking along a road at sunrise" points="762,0 1120,0 1120,212 762,212 706,106" fill="url(#photo-tone)"/>
      <polyline class="photo-edge" points="757,0 701,106 757,212" fill="none" stroke="var(--panel-white)" stroke-width="3"/>
    </svg>

    <div class="brand-block">
      <div class="brand-number">712<br>35</div>
      <div class="brand-descriptor">COMMERCE PARK</div>
      <div class="partner-row">
        <span class="partner"><span class="partner-dot"></span>RLW GROUP</span>
        <span class="partner"><span class="partner-square"></span>MERO</span>
      </div>
    </div>

    <h1 class="headline">Building a<br>Sustainable<br>Future</h1>
  </div>
</body>
</html>
```